依頼詳細
アーチャー用LPイメージ:
https://mockview.example-pinora.com/view/3b7e2a1d-5c90-4f18-a6e2-7d41c9b0e5a2-d17f/

メンバー用LPイメージ:
https://mockview.example-pinora.com/view/8f2c6d4e-1a37-4b95-8c0d-2e69f5a7b314-9e2a/

TOPの写真から虹色のラインの所までのイメージをillustratorか、フォトショップで作成お願いします。

TOP用写真と、アイコンのロゴは添付いたします。
記載項目
XDのテキスト通りでお願いします。
サイズ
• サイズは加工するので、やや大きめでスマホ版TOP、PC版TOPに使えるサイズ感でお願いします。
希望イメージ
シンプル 複雑
単色 カラフル
暗い 明るい
日常 高級
遊び心 厳粛
未来的 伝統的
女性的 男性的
希望する色
虹色
納品ファイル
• イラストレーター形式 (.ai)
• フォトショップ形式 (.psd)
補足説明
今週中には確定したいと思います。
宜しくお願い致します。
ご応募が少なかったので延長させていただきます!
LPすべてではなく、TOPの画像のみなので、気軽にご応募いただけると幸いです。
■ 選んだ理由

素敵なデザインを提案いただきありがとうございました。
内容が分かりやすく、デザインもイメージに合いましたので選ばせていただきました。
今回お二人選ばせていただきましたが、どちらがという事ではなくお二人とも気に入りましたので、
お二人を当選とさせていただき、ユーザーへのABテストを行なっていこうと思います。
本当にありがとうございました!

■ 提案者全員のお礼・コメント

ご提案いただき誠にありがとうございました。
虹色の使い方が難しかったと思いますが、皆様それぞれ素晴らしいご提案をしていただき、本当に感謝しております。
大変迷いましたが、今回2名の方を当選させていただきました。
本当にありがとうございました。

```html
<!DOCTYPE html>
<html lang="ja">
<head>
<meta charset="UTF-8">
<title>クイヴェラ 婚活マッチングアプリ</title>
<link href="https://fonts.googleapis.com/css2?family=M+PLUS+Rounded+1c:wght@400;500;700&family=Noto+Sans+JP:wght@400;500;700&display=swap" rel="stylesheet">
<style>
:root{
  --pink:#f06a9b;
  --pink-soft:rgba(244,143,177,.72);
  --white:#ffffff;
  --ink:#555555;
  --grey:#9a9a9a;
  --line:#d8c7b0;
  --rb-1:#ffd36e;
  --rb-2:#ff9ec4;
  --rb-3:#c9a3ff;
  --rb-4:#8fd3ff;
  --rb-5:#a6f0c8;
  --badge:#111111;
}
*{margin:0;padding:0;box-sizing:border-box}
html,body{width:675px;height:1200px;overflow:hidden;background:var(--white)}
body{font-family:"Noto Sans JP",sans-serif;color:var(--ink);position:relative}
.page{position:relative;width:675px;height:1200px;overflow:hidden}
.hero-photo{position:absolute;left:0;top:0;width:675px;height:640px;
  background:
   linear-gradient(to bottom,rgba(255,255,255,0) 55%,#fff 100%),
   radial-gradient(circle at 30% 35%,#f3d7c6 0,transparent 35%),
   radial-gradient(circle at 65% 25%,#e8c9b6 0,transparent 30%),
   linear-gradient(135deg,#e9e4dc,#f6efe8 50%,#dcd3c8)}
.header{position:absolute;left:0;top:0;width:675px;height:70px;
  background:linear-gradient(90deg,var(--rb-1),var(--rb-2) 30%,var(--rb-3) 60%,var(--rb-4));
  display:flex;align-items:center;justify-content:center}
.menu-icon{position:absolute;left:24px;top:22px}
.site-title{font-family:"M PLUS Rounded 1c",sans-serif;font-weight:500;font-size:36px;color:var(--white)}
.login{position:absolute;right:18px;top:12px;width:140px;height:44px;border-radius:6px;
  background:var(--white);font-size:24px;color:var(--ink);display:flex;align-items:center;justify-content:center}
.catch{position:absolute;left:50px;top:405px;width:580px;height:205px;background:var(--pink-soft);
  border:2px solid rgba(255,255,255,.7);text-align:center;color:var(--white);
  font-family:"M PLUS Rounded 1c",sans-serif;font-weight:700}
.catch-lead{font-size:35px;line-height:46px;margin-top:14px}
.catch-new{font-size:26px;line-height:32px;margin-top:2px}
.catch-main{font-size:50px;line-height:62px}
.brand-name{position:absolute;left:0;width:675px;top:648px;text-align:center;font-size:36px;color:var(--ink)}
.brand-mark{position:absolute;left:287px;top:705px;width:100px;height:100px;border:2px solid #ddd;border-radius:14px;
  display:flex;align-items:center;justify-content:center;flex-direction:column;gap:4px}
.brand-dot{width:40px;height:40px;border-radius:50%;background:var(--rb-3)}
.brand-word{font-size:16px;color:var(--ink)}
.benefits{position:absolute;left:112px;top:826px;width:450px;list-style:none}
.benefits li{display:flex;align-items:center;gap:18px;height:66px;border-bottom:2px solid var(--line);
  font-family:"M PLUS Rounded 1c",sans-serif;font-weight:500;font-size:36px;color:var(--pink)}
.cta-band{position:absolute;left:0;top:1000px;width:675px;height:200px;
  background:linear-gradient(90deg,var(--rb-1),var(--rb-2) 25%,var(--rb-3) 55%,var(--rb-4) 80%,var(--rb-5))}
.cta-title{text-align:center;color:var(--white);font-size:32px;margin-top:14px;letter-spacing:1px}
.stores{display:flex;gap:14px;margin:14px 0 0 100px}
.store{width:228px;height:66px;background:var(--badge);border-radius:10px;color:var(--white);
  display:flex;flex-direction:column;justify-content:center;padding-left:30px}
.store small{font-size:14px}
.store b{font-size:26px;font-weight:500;line-height:28px}
.notes{position:absolute;left:36px;bottom:8px;width:610px;font-size:16px;color:var(--white);line-height:24px}
.notes .right{position:absolute;right:0;bottom:0}
</style>
</head>
<body>
<div class="page">
  <div class="hero-photo" role="img" aria-label="Photo of smiling couples in bright wedding-style attire at a party"></div>

  <header class="header">
    <svg class="menu-icon" width="40" height="28" viewBox="0 0 40 28"><g stroke="#fff" stroke-width="3"><line x1="0" y1="2" x2="40" y2="2"/><line x1="0" y1="14" x2="40" y2="14"/><line x1="0" y1="26" x2="40" y2="26"/></g></svg>
    <span class="site-title">Quivera</span>
    <span class="login">ログイン</span>
  </header>

  <section class="catch">
    <p class="catch-lead">婚活サポーターが<br>素敵なご縁をサポートする</p>
    <p class="catch-new">\ 新しい /</p>
    <p class="catch-main">婚活マッチングアプリ</p>
  </section>

  <p class="brand-name">クイヴェラ</p>
  <div class="brand-mark"><span class="brand-dot"></span><span class="brand-word">Quivera</span></div>

  <ul class="benefits">
    <li><svg width="28" height="24" viewBox="0 0 28 24"><path d="M2 12l8 9L26 2" fill="none" stroke="#9a9a9a" stroke-width="3"/></svg>登録費・月額費無料!</li>
    <li><svg width="28" height="24" viewBox="0 0 28 24"><path d="M2 12l8 9L26 2" fill="none" stroke="#9a9a9a" stroke-width="3"/></svg>スマホ1つで始められる!</li>
  </ul>

  <section class="cta-band">
    <p class="cta-title">無料でダウンロード、無料で登録。</p>
    <div class="stores">
      <div class="store"><small>からダウンロード</small><b>AppShelf</b></div>
      <div class="store"><small>で手に入れよう</small><b>PlayMarket</b></div>
    </div>
    <div class="notes">
      <p>FaceNote・TalkLineには一切投稿されません</p>
      <p>利用規約/プライバシーポリシー</p>
      <span class="right">※18歳未満の方は登録できません</span>
    </div>
  </section>
</div>
</body>
</html>
```